KT Design Business Card

I would like a business card similar to this
https://www.artquorra.com/design/8173920
with my info and a picture of my rifle. You can use something like this
https://www.snaplirra.com/pin/381926405572018843/visual-search/?cropSource=6&h=476&w=268&x=12&y=12
or
https://www.snaplirra.com/pin/219604837751093468/

I have a logo, it is a shepperds staff. I build custom rifles and do Law Enforcement sales. Some where on the card it needs to say something like, "Custom AR's built correctly", "All rifles come with honed uppers and bedded barrels", "All rifles are fully tested and come with a 3 shot card", "Law Enforcement models are available", "Tactical Equipment Consulting", "One stop shop for all tactical equipment"

Business Name: KT Design LLC
Name: Brent Hollis
Phone: (555) 614-2980
Email: brent.ktdesign@mailbriq.com
Address: 3082 Tamblin Ct., Fernwick, KR, 29815

Just use the concept of the staff in the attachments the other stuff is not related

```html
<!DOCTYPE html>
<html lang="en">
<head>
<meta charset="utf-8">
<title>KT Design Business Card</title>
<link rel="stylesheet" href="https://fonts.googleapis.com/css2?family=Lato:wght@400;700&display=swap">
<style>
  :root {
    --backdrop: #d9d9d9;
    --card: #ffffff;
    --ink: #1a1a1a;
    --rule: #e2e2e2;
    --band: #0d0d0d;
    --photo-light: #f1f1f1;
    --photo-mid: #cfcfcf;
    --photo-dark: #6a6a6a;
  }
  * { margin: 0; padding: 0; box-sizing: border-box; }
  html, body {
    width: 1200px; height: 802px; overflow: hidden;
    background: var(--backdrop);
  }
  .canvas {
    position: relative; width: 1200px; height: 802px;
    font-family: 'Lato', Arial, sans-serif; color: var(--ink);
  }
  .card {
    position: absolute; top: 238px;
    width: 545px; height: 326px;
    background: var(--card); overflow: hidden;
  }
  .card--front { left: 40px; }
  .card--back { left: 615px; }

  .brand-name {
    position: absolute; right: 38px; top: 166px;
    display: flex; align-items: center; gap: 10px;
    font-weight: 700; font-size: 26px; white-space: nowrap;
    color: var(--ink);
  }
  .brand-name::before {
    content: ""; width: 14px; height: 14px; background: var(--ink);
  }
  .holder-name {
    position: absolute; left: 33px; top: 196px;
    font-size: 22px; font-weight: 700; letter-spacing: 0.3px;
  }
  .holder-rule {
    position: absolute; left: 212px; top: 211px;
    width: 295px; height: 1px; background: var(--rule);
  }
  .contact {
    position: absolute; left: 33px;
    display: flex; align-items: center; gap: 6px;
    font-size: 15px; white-space: nowrap;
  }
  .contact svg { width: 14px; height: 14px; fill: var(--ink); flex: none; }
  .contact--phone { top: 233px; }
  .contact--email { top: 254px; }
  .contact--address { top: 283px; }
  .front-band {
    position: absolute; left: 0; bottom: 0;
    width: 100%; height: 12px; background: var(--band);
  }

  .rifle-photo {
    position: absolute; right: 0; top: 0;
    width: 265px; height: 322px;
    background:
      radial-gradient(ellipse 35% 60% at 55% 45%, rgba(106,106,106,0.55) 0%, rgba(106,106,106,0) 75%),
      linear-gradient(90deg, var(--card) 0%, var(--photo-light) 30%, var(--photo-mid) 100%);
  }
  .back-title {
    position: absolute; left: 31px; top: 70px;
    font-weight: 700; font-size: 44px; white-space: nowrap;
  }
  .feature-list {
    position: absolute; left: 29px; top: 162px;
    list-style: none; font-size: 15.5px; line-height: 22.2px;
  }
  .feature-list li { display: flex; align-items: center; white-space: nowrap; }
  .feature-list li::before {
    content: ""; width: 7px; height: 7px; border-radius: 50%;
    background: var(--ink); margin-right: 5px; flex: none;
  }
  .back-band {
    position: absolute; left: 0; bottom: 0;
    width: 100%; height: 4px; background: var(--band);
  }
</style>
</head>
<body>
<div class="canvas">
  <section class="card card--front">
    <div class="brand-name">KT Design</div>
    <h1 class="holder-name">BRENT HOLLIS</h1>
    <div class="holder-rule"></div>
    <div class="contact contact--phone">
      <svg viewBox="0 0 24 24" aria-hidden="true"><path d="M6.6 10.8a15.1 15.1 0 0 0 6.6 6.6l2.2-2.2a1 1 0 0 1 1-.25 11.4 11.4 0 0 0 3.6.57 1 1 0 0 1 1 1V20a1 1 0 0 1-1 1A17 17 0 0 1 3 4a1 1 0 0 1 1-1h3.5a1 1 0 0 1 1 1c0 1.25.2 2.45.57 3.57a1 1 0 0 1-.25 1z"/></svg>
      <span>(555) 614-2980</span>
    </div>
    <div class="contact contact--email">
      <svg viewBox="0 0 24 24" aria-hidden="true"><path d="M2 5h20v14H2zm2 2v.5l8 5 8-5V7zm0 2.8V17h16V9.8l-8 5z"/></svg>
      <span>brent.ktdesign@mailbriq.com</span>
    </div>
    <div class="contact contact--address">
      <svg viewBox="0 0 24 24" aria-hidden="true"><path d="M12 2a7 7 0 0 0-7 7c0 5.25 7 13 7 13s7-7.75 7-13a7 7 0 0 0-7-7zm0 9.5A2.5 2.5 0 1 1 12 6.5a2.5 2.5 0 0 1 0 5z"/></svg>
      <span>3082 Tamblin Ct., Fernwick, KR, 29815</span>
    </div>
    <div class="front-band"></div>
  </section>

  <section class="card card--back">
    <div class="rifle-photo" role="img" aria-label="Photo of a custom built rifle lying on a light concrete surface"></div>
    <h2 class="back-title">KT Design</h2>
    <ul class="feature-list">
      <li>Custom rifles assembled with care</li>
      <li>Agency and duty models on request</li>
      <li>Tactical gear advice and planning</li>
      <li>Every tactical need covered in one place</li>
      <li>Each rifle gets a honed upper and bedded barrel</li>
      <li>Each rifle is range tested and ships with a group card</li>
    </ul>
    <div class="back-band"></div>
  </section>
</div>
</body>
</html>
```